" A Rumo ao Horizonte é uma empresa que trabalha com curso, treinamentos e palestras com o objetivo de desenvolvimento pessoal e aumentar o nível de vibração pessoal. "

```html
<!DOCTYPE html>
<html lang="pt-BR">
<head>
<meta charset="utf-8">
<title>Rumo ao Horizonte — Cartão de visita</title>
<link href="https://fonts.googleapis.com/css2?family=Questrial&display=swap" rel="stylesheet">
<style>
  :root {
    --page-bg: #f6f6f7;
    --card-front: #ffffff;
    --card-back: #e3e3e5;
    --deco-light: #f1f1f2;
    --deco-mid: #e6e6e8;
    --brand-purple: #6a3d84;
    --ink: #545457;
    --icon-bg: #4e4e52;
    --icon-fg: #e3e3e5;
  }
  * { margin: 0; padding: 0; box-sizing: border-box; }
  html, body {
    width: 1200px;
    height: 1200px;
    overflow: hidden;
    background: var(--page-bg);
    font-family: "Questrial", "Century Gothic", sans-serif;
  }
  .card {
    position: absolute;
    left: 173px;
    width: 845px;
    height: 466px;
    border-radius: 24px;
    overflow: hidden;
  }
  .card--front {
    top: 106px;
    background: var(--card-front);
  }
  .card--back {
    top: 631px;
    background: var(--card-back);
  }
  .front-backdrop {
    position: absolute;
    inset: 0;
    background:
      radial-gradient(ellipse 60% 95% at 18% 55%, var(--deco-mid) 0%, var(--deco-light) 55%, rgba(255,255,255,0) 80%);
  }
  .front-brand {
    position: absolute;
    left: 0;
    right: 0;
    top: 330px;
    text-align: center;
    font-size: 50px;
    line-height: 1;
    color: var(--brand-purple);
  }
  .front-brand-dot {
    position: absolute;
    left: 50%;
    top: 210px;
    width: 92px;
    height: 92px;
    margin-left: -46px;
    border-radius: 50%;
    background: var(--brand-purple);
  }
  .holder-name {
    position: absolute;
    left: 50px;
    top: 108px;
    font-size: 36px;
    color: var(--ink);
    letter-spacing: 0.5px;
  }
  .contact-list {
    position: absolute;
    left: 58px;
    top: 280px;
    list-style: none;
  }
  .contact-item {
    display: flex;
    align-items: center;
    height: 34px;
    font-size: 24px;
    color: var(--ink);
  }
  .contact-icon {
    width: 22px;
    height: 22px;
    margin-right: 18px;
    flex: none;
  }
  .back-brand {
    position: absolute;
    right: 42px;
    top: 325px;
    font-size: 28px;
    color: var(--ink);
  }
</style>
</head>
<body>

<section class="card card--front">
  <div class="front-backdrop" role="img" aria-label="Grande elemento decorativo suave em tons de cinza claro"></div>
  <div class="front-brand-dot"></div>
  <p class="front-brand">Rumo ao Horizonte</p>
</section>

<section class="card card--back">
  <h1 class="holder-name">Helena Duarte</h1>
  <ul class="contact-list">
    <li class="contact-item">
      <svg class="contact-icon" viewBox="0 0 22 22" aria-hidden="true">
        <rect width="22" height="22" rx="3" fill="var(--icon-bg)"/>
        <rect x="7" y="4" width="8" height="14" rx="1.5" fill="none" stroke="var(--icon-fg)" stroke-width="1.8"/>
        <circle cx="11" cy="15.5" r="1" fill="var(--icon-fg)"/>
      </svg>
      31 90000-4127
    </li>
    <li class="contact-item">
      <svg class="contact-icon" viewBox="0 0 22 22" aria-hidden="true">
        <rect width="22" height="22" rx="3" fill="var(--icon-bg)"/>
        <circle cx="11" cy="11" r="2.6" fill="none" stroke="var(--icon-fg)" stroke-width="1.6"/>
        <path d="M13.6 9v3.2c0 1.6 2.6 1.8 2.6-0.8A5.2 5.2 0 1 0 13.5 15.6" fill="none" stroke="var(--icon-fg)" stroke-width="1.6"/>
      </svg>
      helena@rumoaohorizonte.com.br
    </li>
    <li class="contact-item">
      <svg class="contact-icon" viewBox="0 0 22 22" aria-hidden="true">
        <rect width="22" height="22" rx="3" fill="var(--icon-bg)"/>
        <circle cx="11" cy="11" r="6" fill="none" stroke="var(--icon-fg)" stroke-width="1.5"/>
        <ellipse cx="11" cy="11" rx="2.5" ry="6" fill="none" stroke="var(--icon-fg)" stroke-width="1.3"/>
        <line x1="5" y1="11" x2="17" y2="11" stroke="var(--icon-fg)" stroke-width="1.3"/>
      </svg>
      www.rumoaohorizonte.com.br
    </li>
  </ul>
  <p class="back-brand">Rumo ao Horizonte</p>
</section>

</body>
</html>
```